Canadian company needs a packaging design for a new product line of TubNova Hot Tub & Bath Fragran

We are looking for a packaging design for a new company based in Edmonton, Alberta Canada called TubNova. We are developing a new product line of liquid and crystal Hot Tub & Bath Fragrances (aromatherapy) for example Lavender will be one of our fragrances. We are looking at the possibilities of using a stand up pouch and or the standard plastic bottles for our fragrance line. There will be different sizes from 150 grams to 600 grams in the crystal and 275 ml in the liquid. We would like to see bright multi-colored designs possibly with picture of the fragrance or a theme like favorite drinks or a more sensual idea. Each one of our fragrances will be a different color the main design needs to be able to have a different color of liquid or crystal in the bottle and possibly parts of the label will change colors for each fragrance. I have attached samples of another brand that we want to improve on.

Target Market(s)

Most of these fragrance are bought by women 70% men 30%
age 25 - 55

Industry/Entity Type

It Company

Requirements
Must have
• bottle size
Fragrance name
Nice to have
• Using the files below I like the circle of colors and possibly it could be made using water drops like in the file and possibly the two "S" could be designed like the third file I just added

```html
<!DOCTYPE html>
<html lang="en">
<head>
<meta charset="utf-8">
<title>TubNova – Coral Lagoon Fragrance Labels</title>
<link rel="stylesheet" href="https://fonts.googleapis.com/css2?family=Fredoka:wght@600&family=Great+Vibes&family=Arimo:wght@400;700&display=swap">
<style>
  :root {
    --backdrop: #e6e8ea;
    --orchid: #a22fb0;
    --orchid-deep: #7c1f8a;
    --lagoon: #2a9ea3;
    --lagoon-deep: #19787e;
    --mark: #23a595;
    --label-light: #eaf7fb;
    --label-sky: #a9e2ee;
    --script-ink: #55399b;
    --size-ink: #2f35a8;
    --white: #ffffff;
  }
  * { box-sizing: border-box; margin: 0; padding: 0; }
  html, body { width: 1022px; height: 1200px; overflow: hidden; }
  body { background: var(--backdrop); position: relative; }

  .label-set { position: absolute; inset: 0; }

  .front-label {
    position: absolute;
    top: 220px;
    width: 420px;
    height: 760px;
    border-radius: 64px;
    overflow: hidden;
  }
  .front-label--orchid { left: 61px;  background: linear-gradient(90deg, var(--orchid-deep), var(--orchid) 20%, var(--orchid) 80%, var(--orchid-deep)); }
  .front-label--lagoon { left: 541px; background: linear-gradient(90deg, var(--lagoon-deep), var(--lagoon) 20%, var(--lagoon) 80%, var(--lagoon-deep)); }

  .brand-dot {
    position: absolute; top: 58px; left: 50%;
    width: 74px; height: 74px; margin-left: -37px;
    border-radius: 50%; background: var(--mark);
    box-shadow: 0 0 0 2px rgba(255, 255, 255, .35);
  }
  .brand-name {
    position: absolute; top: 136px; left: 0; right: 0;
    text-align: center;
    font-family: "Fredoka", sans-serif; font-weight: 600;
    font-size: 54px; line-height: 1; color: var(--white);
  }

  .label-window { position: absolute; top: 210px; left: 0; width: 420px; height: 470px; }

  .fragrance-name {
    position: absolute; top: 262px; left: 0; right: 0;
    text-align: center;
    font-family: "Great Vibes", cursive;
    font-size: 50px; line-height: 1.1; color: var(--script-ink);
    white-space: nowrap;
  }

  .reef-art {
    position: absolute; top: 350px; left: 40px;
    width: 340px; height: 250px;
    border-radius: 10px;
    background:
      radial-gradient(ellipse at 25% 65%, rgba(160, 120, 220, .75), transparent 55%),
      radial-gradient(ellipse at 75% 70%, rgba(240, 170, 60, .7), transparent 50%),
      radial-gradient(ellipse at 50% 90%, rgba(60, 150, 110, .6), transparent 60%),
      linear-gradient(180deg, rgba(169, 226, 238, .4), rgba(90, 180, 150, .55));
  }

  .size-line {
    position: absolute; top: 690px; left: 0; right: 0;
    text-align: center;
    font-family: "Arimo", sans-serif; color: var(--size-ink);
  }
  .size-line .volume { font-weight: 700; font-size: 22px; }
  .size-line .net-weight { font-size: 10px; margin-left: 6px; letter-spacing: .3px; }
</style>
</head>
<body>
<main class="label-set">

  <section class="front-label front-label--orchid">
    <div class="brand-dot"></div>
    <div class="brand-name">TubNova</div>
    <svg class="label-window" viewBox="0 0 420 470" aria-hidden="true">
      <defs>
        <linearGradient id="label-fill-a" x1="0" y1="0" x2="1" y2="1">
          <stop offset="0" stop-color="#c7eef6"/>
          <stop offset="0.5" stop-color="#eaf7fb"/>
          <stop offset="1" stop-color="#a9e2ee"/>
        </linearGradient>
      </defs>
      <path d="M30 20 Q210 70 390 20 L390 440 Q210 395 30 440 Z" fill="url(#label-fill-a)"/>
    </svg>
    <div class="fragrance-name">Coral Lagoon</div>
    <div class="reef-art" role="img" aria-label="Underwater illustration of coral, seaweed and small fish"></div>
    <div class="size-line"><span class="volume">300ml</span><span class="net-weight">NET WT: 150</span></div>
  </section>

  <section class="front-label front-label--lagoon">
    <div class="brand-dot"></div>
    <div class="brand-name">TubNova</div>
    <svg class="label-window" viewBox="0 0 420 470" aria-hidden="true">
      <defs>
        <linearGradient id="label-fill-b" x1="0" y1="0" x2="1" y2="1">
          <stop offset="0" stop-color="#c7eef6"/>
          <stop offset="0.5" stop-color="#eaf7fb"/>
          <stop offset="1" stop-color="#a9e2ee"/>
        </linearGradient>
      </defs>
      <path d="M30 20 Q210 70 390 20 L390 440 Q210 395 30 440 Z" fill="url(#label-fill-b)"/>
    </svg>
    <div class="fragrance-name">Coral Lagoon</div>
    <div class="reef-art" role="img" aria-label="Underwater illustration of coral, seaweed and small fish"></div>
    <div class="size-line"><span class="volume">300ml</span><span class="net-weight">NET WT: 150</span></div>
  </section>

</main>
</body>
</html>
```